real esate business card with company logo and name

we need a business card design for a real esate company

The company name is Walsh & Brody Pty Ltd, and we have our logo designed and will upload. We want classic or moden feel. Black or white background. looks more textured. Should include folowinginformations
Paul Walsh and Lucy Brody
Sales Agents & Onsite Manager
p: 07 5948 2063
F: 07 5948 2174
M:0461 857 239
3/42 Marlin Crescent, ELLEN GROVE QLD 4078

We want this business card looks professonal. Thank you in advance.

Industry/Entity Type

Real Estate Agent

Contact Information for Business Card

Paul Walsh and Lucy Brody
Onsite Manager & Sales Agents
p: 07 5948 2063
M:0461 857 239

Font styles to use
Serif

Colors
000000
fbfbfb
333333
959595

Requirements
Must have
• company logo and name, black or white back ground

```html
<!DOCTYPE html>
<html lang="en">
<head>
<meta charset="utf-8">
<title>Walsh &amp; Brody Pty Ltd — Business Card</title>
<link rel="stylesheet" href="https://fonts.googleapis.com/css2?family=Open+Sans:wght@400;600&family=Oswald:wght@400&display=swap">
<style>
  :root {
    --stage: #3b3431;
    --card-black: #000000;
    --card-deep: #111111;
    --ink-light: #fbfbfb;
    --ink-mid: #959595;
    --ink-dark: #333333;
  }
  * { box-sizing: border-box; margin: 0; padding: 0; }
  html, body { width: 1200px; height: 844px; overflow: hidden; }
  body {
    background: var(--stage);
    font-family: "Open Sans", Arial, sans-serif;
    position: relative;
  }
  .card {
    position: absolute;
    top: 257px;
    width: 540px;
    height: 330px;
    border-radius: 3px;
    background:
      radial-gradient(ellipse at 30% 20%, #1b1b1b 0%, var(--card-deep) 45%, var(--card-black) 100%);
    box-shadow: 0 14px 30px rgba(0,0,0,0.45);
    overflow: hidden;
  }
  .card--front { left: 40px; }
  .card--back { left: 620px; }

  .brand {
    position: absolute;
    display: flex;
    flex-direction: column;
    align-items: center;
    gap: 16px;
    color: var(--ink-mid);
    font-family: "Oswald", "Arial Narrow", sans-serif;
    font-weight: 400;
    text-transform: uppercase;
    letter-spacing: 0.04em;
    white-space: nowrap;
  }
  .brand__square {
    width: 96px;
    height: 96px;
    background: var(--ink-mid);
    flex: none;
  }
  .card--front .brand {
    left: 255px;
    width: 230px;
    top: 64px;
    font-size: 18px;
  }
  .card--back .brand {
    left: 50%;
    top: 50%;
    transform: translate(-50%, -50%);
    font-size: 20px;
  }
  .card--back .brand__square { width: 104px; height: 104px; }

  .people {
    position: absolute;
    left: 34px;
    top: 40px;
  }
  .people__names {
    color: var(--ink-mid);
    font-weight: 600;
    font-size: 16px;
    line-height: 1.2;
  }
  .people__role {
    color: var(--ink-light);
    font-size: 12.5px;
    margin-top: 2px;
  }

  .contact {
    position: absolute;
    left: 34px;
    bottom: 40px;
    color: var(--ink-light);
    font-size: 14px;
    line-height: 1.4;
    list-style: none;
  }
  .contact__line {
    display: flex;
    align-items: center;
    gap: 10px;
  }
  .contact__icon { width: 14px; height: 14px; flex: none; }
  .contact__address { margin-top: 14px; }
</style>
</head>
<body>
  <section class="card card--front" aria-label="Business card front">
    <div class="people">
      <p class="people__names">Paul Walsh and Lucy Brody</p>
      <p class="people__role">Onsite Manager &amp; Sales Agents</p>
    </div>

    <div class="brand">
      <span class="brand__square" aria-hidden="true"></span>
      <span class="brand__name">Walsh &amp; Brody Pty Ltd.</span>
    </div>

    <ul class="contact">
      <li class="contact__line">
        <svg class="contact__icon" viewBox="0 0 16 16" aria-hidden="true">
          <path fill="#959595" d="M2 6c0-2 2.5-3 6-3s6 1 6 3v1h-3V5.5H5V7H2z"/>
          <rect x="3.5" y="8" width="9" height="6" rx="1" fill="#959595"/>
        </svg>
        <span>07 5948 2063</span>
      </li>
      <li class="contact__line">
        <svg class="contact__icon" viewBox="0 0 16 16" aria-hidden="true">
          <rect x="4" y="1" width="8" height="14" rx="1.5" fill="none" stroke="#959595" stroke-width="1.5"/>
          <circle cx="8" cy="12.5" r="0.9" fill="#959595"/>
        </svg>
        <span>0461 857 239</span>
      </li>
      <li class="contact__address">3/42 Marlin Crescent,<br>ELLEN GROVE QLD 4078</li>
    </ul>
  </section>

  <section class="card card--back" aria-label="Business card back">
    <div class="brand">
      <span class="brand__square" aria-hidden="true"></span>
      <span class="brand__name">Walsh &amp; Brody Pty Ltd.</span>
    </div>
  </section>
</body>
</html>
```